IT’S NOT A CLEANING, IT’S YOUR LIFE! TOP TEN REASONS WHY THIS IS NOT JUST A “CLEANING”

We made a list for our patients to let them know why our hygiene appointments are different than other cleanings. Since this is a lot of information, we would like it easily readable within 4-5 feet but we do not want the post to be HUGE. Please see below:

IT’S NOT A CLEANING, IT’S YOUR LIFE!
TOP TEN REASONS WHY THIS IS NOT JUST A “CLEANING”

10. We make you look better. Healthy teeth and gums are more attractive. Recent studies
show that the smile is the first thing people notice and that people with better looking teeth
are more confident and successful.

9. We can relieve your headaches. During your hygiene visit we evaluate for serious bite
issues, many of which lead to muscle soreness, headaches, and migraines.

8. We check for oral cancer. Oral cancer kills 1 person per hour 24 hours a day. The death rate for oral cancer is higher than cancers we routinely hear about such as cervical, thyroid and skin cancer.

7. We make you smell better. During your hygiene visit we eliminate many of the germs that live under your gum tissue and cause bad breath.

6. We save you money. By utilizing the latest dental technology (digital x-rays, mouth
cameras, and magnification glasses) we can help with early detection of tooth and gum
problems and save you the cost of gum surgery, root canals, and implants.

5. We clean in places you cannot. We clean under the gum line and between teeth where
most of the germs hide and cause dental disease. 40% of the bacteria in your mouth lives in
between your teeth.

4. We prevent pain. We identify tooth decay that can lead to nerve involvement and pain,
root canal, and tooth loss.

3. We save your teeth. Most tooth loss is from periodontal/gum disease. At each visit we
evaluate the health of your gums and bone with our periodontal screening. Periodontal
disease, like high blood pressure, is symptomless until it is in advanced stages.

2. We protect your loved ones. Studies have proven that the bacteria that cause dental
disease can be transmitted from person to person. Think about that the next time you kiss
someone!

1. We prolong life. Researchers have linked the inflammation and infection found in the
mouth to heart attacks, strokes, and Alzheimer’s. By reducing infection in your mouth we can
greatly improve your overall health!

```html
<!DOCTYPE html>
<html lang="en">
<head>
<meta charset="utf-8">
<title>It's Not a Cleaning, It's Your Life!</title>
<link rel="stylesheet" href="https://fonts.googleapis.com/css2?family=Montserrat:wght@800&family=Arimo:wght@400;700&display=swap">
<style>
  :root {
    --mint-bg: #e4f5ec;
    --brand-green: #1ea46f;
    --panel-white: #ffffff;
    --ink: #1a1a1a;
  }
  html, body {
    margin: 0;
    padding: 0;
    width: 1200px;
    height: 2400px;
    overflow: hidden;
  }
  body {
    background: var(--mint-bg);
    position: relative;
    font-family: "Arimo", Arial, sans-serif;
    color: var(--ink);
  }
  .poster-panel {
    position: absolute;
    left: 62px;
    top: 48px;
    width: 1076px;
    height: 2312px;
    box-sizing: border-box;
    background: var(--panel-white);
    border: 6px solid var(--brand-green);
  }
  .headline {
    margin: 110px 0 0;
    text-align: center;
    font-family: "Montserrat", "Arial Black", sans-serif;
    font-weight: 800;
    font-size: 92px;
    line-height: 1.12;
    letter-spacing: 1px;
    color: var(--brand-green);
  }
  .subheading {
    margin: 88px 0 0;
    text-align: center;
    font-family: "Arimo", Arial, sans-serif;
    font-weight: 700;
    font-size: 26px;
    letter-spacing: 0.3px;
  }
  .reasons-list {
    list-style: none;
    margin: 42px 0 0 88px;
    padding: 0;
    width: 900px;
  }
  .reason {
    font-size: 29px;
    line-height: 1.3;
    margin-bottom: 36px;
  }
</style>
</head>
<body>
  <main class="poster-panel">
    <h1 class="headline">IT’S NOT A CLEANING,<br>IT’S YOUR LIFE!</h1>
    <h2 class="subheading">TOP TEN REASONS WHY THIS IS NOT JUST A “CLEANING”</h2>
    <ol class="reasons-list">
      <li class="reason">10. We make you look better. Healthy teeth and gums are more attractive. Recent studies show that the smile is the first thing people notice and that people with better looking teeth are more confident and successful.</li>
      <li class="reason">9. We can relieve your headaches. During your hygiene visit we evaluate for serious bite issues, many of which lead to muscle soreness, headaches, and migraines.</li>
      <li class="reason">8. We check for oral cancer. Oral cancer kills 1 person per hour 24 hours a day. The death rate for oral cancer is higher than cancers we routinely hear about such as cervical, thyroid and skin cancer.</li>
      <li class="reason">7. We make you smell better. During your hygiene visit we eliminate many of the germs that live under your gum tissue and cause bad breath.</li>
      <li class="reason">6. We save you money. By utilizing the latest dental technology (digital x-rays, mouth cameras, and magnification glasses) we can help with early detection of tooth and gum problems and save you the cost of gum surgery, root canals, and implants.</li>
      <li class="reason">5. We clean in places you cannot. We clean under the gum line and between teeth where most of the germs hide and cause dental disease. 40% of the bacteria in your mouth lives in between your teeth.</li>
      <li class="reason">4. We prevent pain. We identify tooth decay that can lead to nerve involvement and pain, root canal, and tooth loss.</li>
      <li class="reason">3. We save your teeth. Most tooth loss is from periodontal/gum disease. At each visit we evaluate the health of your gums and bone with our periodontal screening. Periodontal disease, like high blood pressure, is symptomless until it is in advanced stages.</li>
      <li class="reason">2. We protect your loved ones. Studies have proven that the bacteria that cause dental disease can be transmitted from person to person. Think about that the next time you kiss someone!</li>
      <li class="reason">1. We prolong life. Researchers have linked the inflammation and infection found in the mouth to heart attacks, strokes, and Alzheimer’s. By reducing infection in your mouth we can greatly improve your overall health!</li>
    </ol>
  </main>
</body>
</html>
```